Kovrix - consultancy website

I need a new design for my webpage/presence [to be functioning with Wordpress - I have a programmer to set it up but not the design idea].
My company is Kovrix - a consultancy firm focused on growth management for Swedish SME's primarily;. We call it Leadership add-on for firms on the rise, kind of a doctor helping small become big. Contentwise, its a simple frontpage + 3-4 subpages with content re company/myself/focus etc. The new site should communicate a fresh, trustworthy take yet simple and functional on all devices [i.e. think UI compatible for mobile/tablet]. Current building parts/form elements are
a) existing logo and text elements
b) existing pictures
c) the yellowish color
colours and new ideas on pictures/positioning are welcome. I prefer a 'full width page' solution with centralised text elements but that's all up to you to suggest. Current site is a quickfix made by myself - now I'm moving it to a new platform so want to take the opportunity to make it
Nothing superspecial as it is a 2-man show; on the other hand I still want to have a modern & fresh reflection of my brand in digital environments. Help me out!
www.kovrix-demo.se
Best
Lotta Bergqvalm

```html
<!DOCTYPE html>
<html lang="en">
<head>
<meta charset="utf-8">
<title>Kovrix – Leadership add-on for firms on the rise</title>
<link href="https://fonts.googleapis.com/css2?family=Noto+Serif:ital,wght@0,400;0,700;1,400&family=Open+Sans:wght@400;600;700&display=swap" rel="stylesheet">
<style>
:root{
  --orange:#f39a1e;
  --ink:#2f3237;
  --text:#6b6f75;
  --muted:#9a9ea4;
  --line:#e6e6e6;
  --paper:#ffffff;
  --footer:#2b2c2f;
  --footer-text:#a5a7ab;
  --serif:"Noto Serif", Georgia, serif;
  --sans:"Open Sans", Arial, sans-serif;
}
*{box-sizing:border-box;margin:0;padding:0}
html,body{width:1200px;height:2752px;overflow:hidden}
body{font-family:var(--sans);color:var(--text);background:var(--paper);font-size:14px;line-height:1.7}

/* header */
.site-header{height:88px;display:flex;align-items:center;justify-content:space-between;padding:0 40px 0 36px;background:var(--paper)}
.brand{font-family:var(--serif);font-weight:700;font-size:40px;color:var(--ink);letter-spacing:-.5px}
.main-nav{display:flex}
.main-nav a{font-size:12px;font-weight:600;color:var(--ink);text-decoration:none;letter-spacing:.6px;padding:32px 20px;border-bottom:3px solid transparent}
.main-nav a.is-active{border-bottom-color:var(--orange);color:var(--orange)}

/* hero */
.hero{height:520px;position:relative;overflow:hidden}
.hero-photo{position:absolute;inset:0;background:linear-gradient(180deg,#a3a6aa 0%,#84888d 50%,#55595e 100%)}
.hero-copy{position:absolute;left:150px;top:300px;color:#fff}
.hero-copy h1{font-family:var(--serif);font-weight:700;font-size:44px;line-height:1.15}
.hero-copy p{font-size:13px;margin-top:16px;max-width:480px;line-height:1.6}
.slider-arrow{position:absolute;top:240px;width:36px;height:36px;border-radius:50%;background:rgba(255,255,255,.2);display:flex;align-items:center;justify-content:center}
.slider-arrow.prev{left:20px}.slider-arrow.next{right:20px}

/* section title */
.section-title{font-family:var(--serif);font-weight:700;font-size:32px;color:var(--ink);text-align:center;letter-spacing:1px}
.title-rule{width:60px;height:2px;background:var(--orange);margin:10px auto 0}

/* services */
.services{height:452px;padding-top:56px}
.services .intro{width:900px;margin:18px auto 0;text-align:center;font-size:12.5px;line-height:1.65}
.service-grid{display:flex;justify-content:center;gap:40px;margin-top:44px}
.service{width:210px;text-align:center}
.service-icon{width:88px;height:88px;border-radius:50%;background:var(--orange);margin:0 auto;display:flex;align-items:center;justify-content:center;box-shadow:0 0 0 5px #fde7c6}
.service h3{font-family:var(--serif);font-size:15px;color:var(--ink);font-weight:400;margin-top:22px}
.service p{font-size:12px;margin-top:8px;line-height:1.6}

/* about */
.about{height:320px;position:relative;color:#fff;text-align:center;overflow:hidden}
.about-photo{position:absolute;inset:0;background:linear-gradient(180deg,#262b33 0%,#16181c 60%,#1d1b18 100%)}
.about-inner{position:relative;padding-top:70px}
.about .section-title{color:#fff}
.about p{width:900px;margin:22px auto 0;font-size:12.5px;line-height:1.7}
.btn-outline{display:inline-flex;align-items:center;gap:8px;margin-top:24px;padding:7px 20px;border:1px solid rgba(255,255,255,.8);border-radius:16px;font-size:11px;letter-spacing:1px;color:#fff}

/* testimonial */
.testimonial{height:440px;padding-top:66px;text-align:center;position:relative}
.testimonial .section-title{font-size:30px;letter-spacing:0}
.testimonial blockquote{width:820px;margin:34px auto 0;font-family:var(--serif);font-style:italic;font-size:15px;line-height:1.75}
.quote-author{display:flex;align-items:center;justify-content:center;gap:22px;margin-top:40px}
.quote-author .name{font-weight:600;color:var(--ink);font-size:14px}
.quote-author .role{font-size:13px;color:var(--muted)}
.avatar{width:72px;height:72px;border-radius:50%;background:linear-gradient(160deg,#b9bcc0,#5a5e63);border:3px solid #fff;box-shadow:0 0 0 1px var(--line)}
.quote-arrow{position:absolute;top:184px;width:30px;height:30px;border-radius:50%;border:1px solid var(--line);display:flex;align-items:center;justify-content:center}
.quote-arrow.prev{left:50px}.quote-arrow.next{right:50px}

/* tweet band */
.tweet-band{height:140px;background:var(--orange);display:flex;align-items:center;padding-left:170px;color:#fff}
.tweet-badge{width:70px;height:70px;border-radius:50%;background:#fff;flex:none}
.tweet-copy{margin-left:40px;font-size:14px;line-height:1.6}
.tweet-copy .when{font-size:12px;margin-top:4px}

/* who & blog */
.columns{height:440px;display:flex;gap:80px;padding:50px 100px 0}
.column{flex:1}
.column h2{font-family:var(--serif);font-weight:400;font-size:22px;color:var(--ink);padding-bottom:12px;border-bottom:1px solid var(--line);position:relative}
.column h2::after{content:"";position:absolute;left:0;bottom:-1px;width:70px;height:2px;background:var(--orange)}
.who-photo{width:360px;height:190px;margin-top:26px;background:linear-gradient(120deg,#d7dade 0%,#8fa3b5 50%,#3d5a7a 100%)}
.who h3{font-size:14px;font-weight:600;color:var(--ink);margin-top:18px}
.who p{font-size:12.5px;margin-top:6px;width:420px}
.post{display:flex;gap:22px;margin-top:24px;padding-bottom:22px;border-bottom:1px solid var(--line)}
.post:last-child{border-bottom:0}
.post-thumb{width:140px;height:110px;flex:none}
.post-thumb.one{background:linear-gradient(135deg,#d94e8a,#f0a23a 50%,#4aa8d8)}
.post-thumb.two{background:linear-gradient(160deg,#e9e4dc,#b89f7a 60%,#6d5a44)}
.post h4{font-size:14px;font-weight:600;color:var(--ink)}
.post .date{font-size:12px;color:var(--orange);margin-top:2px}
.post p{font-size:12.5px;margin-top:6px}

/* footer */
.site-footer{height:300px;overflow:hidden;background:var(--footer);display:flex;gap:70px;padding:46px 100px 0;color:var(--footer-text);font-size:12.5px}
.footer-col{flex:1}
.footer-col h5{color:#fff;font-size:13px;font-weight:600;letter-spacing:.8px;margin-bottom:20px}
.contact-row{display:flex;gap:14px;align-items:flex-start;margin-bottom:14px;line-height:1.55}
.contact-row svg{flex:none;margin-top:2px}
.field{height:36px;border:1px solid #45474b;border-radius:2px;padding:0 12px;display:flex;align-items:center;color:#7c7f84;margin-bottom:12px;width:290px}
.btn-subscribe{display:inline-block;margin-top:6px;padding:8px 26px;background:#3b3d41;color:#fff;font-size:11px;letter-spacing:1px;font-weight:600}
.recent{padding-bottom:10px;margin-bottom:10px;border-bottom:1px solid #3c3e42;line-height:1.55}
.recent:last-child{border-bottom:0;margin-bottom:0}
.recent .date{color:var(--orange);font-size:11.5px}

.bottom-bar{height:52px;background:var(--orange);display:flex;align-items:center;justify-content:space-between;padding:0 100px;color:#fff;font-size:12px}
.social{display:flex;gap:10px}
.social span{width:26px;height:26px;border-radius:50%;background:#fff;display:block}
</style>
</head>
<body>

<header class="site-header">
  <div class="brand">Kovrix</div>
  <nav class="main-nav">
    <a class="is-active">HOME</a><a>ABOUT US</a><a>WHAT WE DO</a><a>WHO WE ARE</a><a>WHY US</a><a>CONTACT US</a>
  </nav>
</header>

<section class="hero">
  <div class="hero-photo" role="img" aria-label="Photo: businessman with briefcase before a city skyline, next to a burst of bright paint colours"></div>
  <div class="slider-arrow prev"><svg width="12" height="12" viewBox="0 0 12 12"><path d="M8 1 3 6l5 5" stroke="#fff" stroke-width="2" fill="none"/></svg></div>
  <div class="slider-arrow next"><svg width="12" height="12" viewBox="0 0 12 12"><path d="M4 1l5 5-5 5" stroke="#fff" stroke-width="2" fill="none"/></svg></div>
  <div class="hero-copy">
    <h1>Leadership add-on<br>for firms on the rise</h1>
    <p>We help small Swedish companies build the structure, habits and leadership they need to grow with confidence.</p>
  </div>
</section>

<section class="services">
  <h2 class="section-title">WHAT WE DO</h2>
  <div class="title-rule"></div>
  <p class="intro">Kovrix works beside owners of growing firms, adding experienced leadership exactly where it is needed. We plan, steer and follow through so that growth becomes steady, measurable and lasting for the whole team.</p>
  <div class="service-grid">
    <div class="service">
      <div class="service-icon"><svg width="38" height="34" viewBox="0 0 38 34"><rect x="2" y="20" width="7" height="12" fill="#fff"/><rect x="12" y="13" width="7" height="19" fill="#fff"/><rect x="22" y="6" width="7" height="26" fill="#fff"/><rect x="32" y="1" width="4" height="31" fill="#fff"/></svg></div>
      <h3>Growth Management</h3>
      <p>Clear plans and routines that let your company scale without losing control.</p>
    </div>
    <div class="service">
      <div class="service-icon"><svg width="28" height="38" viewBox="0 0 28 38"><path d="M14 2a11 11 0 0 0-6 20v5h12v-5A11 11 0 0 0 14 2z" fill="#fff"/><rect x="9" y="29" width="10" height="3" fill="#fff"/><rect x="10" y="33.5" width="8" height="3" rx="1.5" fill="#fff"/></svg></div>
      <h3>Corporate Communications</h3>
      <p>Messages that build trust with staff, customers and partners as you grow.</p>
    </div>
    <div class="service">
      <div class="service-icon"><svg width="34" height="34" viewBox="0 0 34 34"><rect x="2" y="5" width="30" height="27" rx="3" fill="#fff"/><rect x="2" y="5" width="30" height="8" fill="#fde0b3"/><rect x="8" y="1" width="4" height="8" rx="1" fill="#fff"/><rect x="22" y="1" width="4" height="8" rx="1" fill="#fff"/><g fill="#f39a1e"><rect x="7" y="17" width="5" height="4"/><rect x="15" y="17" width="5" height="4"/><rect x="23" y="17" width="5" height="4"/><rect x="7" y="24" width="5" height="4"/><rect x="15" y="24" width="5" height="4"/></g></svg></div>
      <h3>Project Management</h3>
      <p>Hands-on steering of key projects from first idea to finished result.</p>
    </div>
    <div class="service">
      <div class="service-icon"><svg width="34" height="32" viewBox="0 0 34 32"><rect x="1" y="13" width="7" height="17" fill="#fff"/><path d="M11 14l7-12c2 0 4 2 3 5l-2 6h10c2 0 3 2 2 4l-3 10c-1 2-2 3-4 3H11z" fill="#fff"/></svg></div>
      <h3>Conceptualizing</h3>
      <p>Turning loose ideas into concepts, offers and models ready for market.</p>
    </div>
  </div>
</section>

<section class="about">
  <div class="about-photo" role="img" aria-label="Photo: dark city skyline at dusk"></div>
  <div class="about-inner">
    <h2 class="section-title">ABOUT OUR COMPANY</h2>
    <p>Kovrix is a small consultancy run by two people with long experience of leading companies through change. We step in as an added part of your management team, bring tested methods and an outside view, and stay until the new way of working runs on its own. Think of us as a doctor for growing firms.</p>
    <span class="btn-outline">READ MORE <svg width="8" height="8" viewBox="0 0 8 8"><path d="M2 0l4 4-4 4z" fill="#fff"/></svg></span>
  </div>
</section>

<section class="testimonial">
  <h2 class="section-title">Said About Kovrix</h2>
  <div class="quote-arrow prev"><svg width="8" height="10" viewBox="0 0 8 10"><path d="M6 1 2 5l4 4" stroke="#bbb" stroke-width="1.5" fill="none"/></svg></div>
  <div class="quote-arrow next"><svg width="8" height="10" viewBox="0 0 8 10"><path d="M2 1l4 4-4 4" stroke="#bbb" stroke-width="1.5" fill="none"/></svg></div>
  <blockquote>“ Working with Kovrix gave us the structure we were missing. In one year we doubled our team, kept our culture and finally had time to think ahead. Their calm, practical way of leading made every step feel possible and clear. ”</blockquote>
  <div class="quote-author">
    <span class="name">Jon Dalen</span>
    <div class="avatar" role="img" aria-label="Portrait photo of the client"></div>
    <span class="role">- Manager</span>
  </div>
</section>

<section class="tweet-band">
  <div class="tweet-badge"></div>
  <div class="tweet-copy">
    <p>New on the blog: five signs your company is ready for its next level of leadership and how to prepare for it.</p>
    <p class="when">2 hours ago</p>
  </div>
</section>

<section class="columns">
  <div class="column who">
    <h2>WHO WE ARE</h2>
    <div class="who-photo" role="img" aria-label="Photo: hand holding a magnifying glass over a globe"></div>
    <h3>Two people, one clear focus</h3>
    <p>Lotta and her partner have led and built companies for over twenty years. Today they share that experience with owners who want to grow without losing their way.</p>
  </div>
  <div class="column">
    <h2>Latest Blog</h2>
    <article class="post">
      <div class="post-thumb one" role="img" aria-label="Photo: colourful abstract paint splash"></div>
      <div>
        <h4>Planning for the next hire</h4>
        <p class="date">May 12, 2015</p>
        <p>Why the timing of your first manager hire matters more than the title.</p>
      </div>
    </article>
    <article class="post">
      <div class="post-thumb two" role="img" aria-label="Photo: person at a desk lifting a weight"></div>
      <div>
        <h4>When the owner must step back</h4>
        <p class="date">April 28, 2015</p>
        <p>Letting go of daily tasks is the hardest and most valuable step.</p>
      </div>
    </article>
  </div>
</section>

<footer class="site-footer">
  <div class="footer-col">
    <h5>CONTACT US</h5>
    <div class="contact-row"><svg width="12" height="16" viewBox="0 0 12 16"><path d="M6 0a6 6 0 0 0-6 6c0 4 6 10 6 10s6-6 6-10a6 6 0 0 0-6-6zm0 8.5A2.5 2.5 0 1 1 6 3.5a2.5 2.5 0 0 1 0 5z" fill="#a5a7ab"/></svg><span>Kovrix AB<br>Storgatan 14<br>114 51 Stockholm</span></div>
    <div class="contact-row"><svg width="14" height="14" viewBox="0 0 14 14"><path d="M3 0l3 3-2 2c1 2 3 4 5 5l2-2 3 3-2 3C6 14 0 8 0 2z" fill="#a5a7ab"/></svg><span>+46 8 555 014 20</span></div>
    <div class="contact-row"><svg width="14" height="12" viewBox="0 0 14 12"><rect x="0.5" y="0.5" width="13" height="11" fill="none" stroke="#a5a7ab"/><path d="M1 1l6 5 6-5" stroke="#a5a7ab" fill="none"/></svg><span>info@kovrix-demo.se</span></div>
  </div>
  <div class="footer-col">
    <h5>SIGN UP FOR NEWSLETTER</h5>
    <div class="field">Name</div>
    <div class="field">Email</div>
    <span class="btn-subscribe">SUBSCRIBE</span>
  </div>
  <div class="footer-col">
    <h5>RECENT POSTS</h5>
    <div class="recent"><p>Is your firm ready for a second manager?</p><p class="date">Jun 02, 2015</p></div>
    <div class="recent"><p>Stepping back without losing control</p><p class="date">May 20, 2015</p></div>
    <div class="recent"><p>Simple routines that make growth last</p><p class="date">May 08, 2015</p></div>
  </div>
</footer>

<div class="bottom-bar">
  <span>© 2015 Kovrix. All rights reserved.</span>
  <div class="social"><span></span><span></span><span></span></div>
</div>

</body>
</html>
```